VELDA NUTRITION WEBSITE DESIGN

We need a full design for the website to present the company to customers and partners.
We are ' Velda nutrition" based in New York. We develop Multivitamins, minerals and nutritional supplements to support immunity, general health and longevity. Our products include: Pregnancy supplements, Bone supplements and Iron supplements.
The design should convey trust, natural, health and growth, also relating to the different products that we sell.

I can not download the edited design and the designer didnt submit the last revised version yet.

```html
<!DOCTYPE html>
<html lang="en">
<head>
<meta charset="utf-8">
<title>Velda Nutrition</title>
<link rel="stylesheet" href="https://fonts.googleapis.com/css2?family=Montserrat:wght@400;500;600;700&family=Varela+Round&family=Tinos&display=swap">
<style>
:root{
  --green:#8cc63f;
  --green-dark:#76b02c;
  --purple:#9057ad;
  --blue:#0b3fa6;
  --red:#e1000f;
  --ink:#222222;
  --grey:#555555;
  --white:#ffffff;
}
*{box-sizing:border-box;margin:0;padding:0}
html,body{width:1200px;height:4286px;overflow:hidden;background:var(--white)}
body{position:relative;font-family:"Montserrat",sans-serif;color:var(--ink)}
.abs{position:absolute}
.brand{display:flex;align-items:center;gap:14px;color:var(--ink);font-family:"Montserrat",sans-serif;font-weight:500}
.brand-dot{border-radius:50%;background:var(--green);flex:none}
.brand-name{line-height:1}
.brand-name small{display:block;font-size:.42em;letter-spacing:.3em;margin-top:6px}
.pill{position:absolute;display:flex;align-items:center;justify-content:center;gap:8px;border-radius:30px;color:var(--white);font-family:"Varela Round",sans-serif;background:var(--green)}
.pill-dot{width:22px;height:22px;border-radius:50%;background:rgba(255,255,255,.75)}
.nav a{position:absolute;top:93px;font-size:17px;color:var(--ink);text-decoration:none}
.hero-photo{left:0;top:138px;width:1200px;height:621px;background:linear-gradient(100deg,#c9c4c0 0%,#e8e4e1 35%,#b9b7b3 60%,#8c8e7a 100%)}
.hero-ring{left:679px;top:253px;width:450px;height:450px;border-radius:50%;background:var(--purple)}
.hero-circle{left:671px;top:253px;width:450px;height:450px;border-radius:50%;background:var(--green);color:var(--white);text-align:center}
.hero-title{position:absolute;left:0;right:0;top:162px;font-family:"Varela Round",sans-serif;font-size:50px;font-weight:400}
.hero-text{position:absolute;left:30px;right:30px;top:236px;font-size:19px;line-height:24px}
.dots{left:521px;top:690px;display:flex;gap:14px}
.dots span{width:11px;height:11px;border-radius:50%;background:rgba(255,255,255,.6)}
.dots span:first-child{background:var(--white)}
.section-title{left:0;width:1200px;text-align:center;font-family:"Varela Round",sans-serif;color:var(--ink)}
.arch{position:absolute;top:960px;width:310px;height:326px;border-radius:155px 155px 0 0}
.bottle{position:absolute;top:1030px;width:196px;height:376px;border-radius:26px 26px 18px 18px;background:linear-gradient(90deg,#dcdcdc,#ffffff 40%,#f2f2f2 75%,#cfcfcf)}
.product-title{position:absolute;top:1436px;width:310px;text-align:center;font-size:20px;font-weight:600}
.product-text{position:absolute;top:1470px;width:310px;text-align:center;font-size:13px;line-height:19px;color:var(--ink)}
.btn-order{position:absolute;top:1528px;width:153px;height:38px;border-radius:20px;background:var(--green);color:var(--white);font-size:16px;font-weight:700;display:flex;align-items:center;justify-content:center;letter-spacing:.5px}
.about-title{left:156px;top:1868px;font-size:43px;font-weight:700;color:var(--white)}
.about-text{left:156px;top:1944px;width:440px;font-size:15px;line-height:22.5px;color:var(--white)}
.btn-outline{left:156px;top:2163px;width:144px;height:37px;border:2px solid var(--white);border-radius:20px;color:var(--white);font-size:15px;font-weight:700;display:flex;align-items:center;justify-content:center;letter-spacing:.5px}
.health-photo{left:0;top:2330px;width:1200px;height:594px;background:linear-gradient(90deg,#f4f3f2 0%,#eceae8 40%,#cfcac6 65%,#9a9592 100%)}
.health-title{left:131px;top:2494px;font-size:43px;line-height:53px;font-weight:500;color:var(--ink)}
.health-text{left:131px;top:2616px;width:480px;font-size:15px;line-height:22.5px;color:var(--grey)}
.gallery-item{position:absolute}
.newsletter{left:0;top:3691px;width:1200px;height:241px;background:var(--green);color:var(--white);text-align:center}
.news-title{position:absolute;left:0;right:0;top:44px;font-family:"Varela Round",sans-serif;font-size:35px}
.news-text{position:absolute;left:0;right:0;top:112px;font-size:14px}
.news-input{position:absolute;left:354px;top:148px;width:353px;height:37px;border-radius:20px;background:var(--white);color:var(--ink);font-family:"Tinos",serif;font-size:12px;text-align:left;padding:11px 12px}
.news-btn{position:absolute;left:712px;top:148px;width:103px;height:37px;border-radius:20px;background:#3c3c3c;color:var(--white);font-size:12px;display:flex;align-items:center;justify-content:center}
.foot-head{position:absolute;top:4008px;font-size:20px;font-weight:600;color:var(--ink)}
.foot-list{position:absolute;top:4046px;font-family:"Tinos",serif;font-size:15px;line-height:25px;color:var(--ink);list-style:none}
.social{position:absolute;top:4110px;width:34px;height:34px;border-radius:50%;background:var(--green)}
.contact-row{position:absolute;left:671px;display:flex;gap:16px;font-family:"Tinos",serif;font-size:15px;line-height:21px}
.copyright{left:0;top:4240px;width:1200px;text-align:center;font-family:"Tinos",serif;font-size:13px;color:var(--ink)}
</style>
</head>
<body>

<!-- Header -->
<header>
  <div class="abs brand" style="left:103px;top:42px;font-size:44px">
    <span class="brand-dot" style="width:56px;height:56px"></span>
    <span class="brand-name">Velda<small>NUTRITION</small></span>
  </div>
  <a class="pill" style="left:947px;top:27px;width:153px;height:40px;font-size:17px"><span class="pill-dot"></span>Order Now</a>
  <nav class="nav">
    <a style="left:424px">Home</a>
    <a style="left:526px">About</a>
    <a style="left:632px">Products</a>
    <a style="left:760px">Why Choose us</a>
    <a style="left:945px">Blog</a>
    <a style="left:1037px">Contact</a>
  </nav>
</header>

<!-- Hero -->
<section>
  <div class="abs hero-photo" role="img" aria-label="Smiling pregnant woman in a bedroom holding a supplement bottle and tablets"></div>
  <div class="abs hero-ring"></div>
  <div class="abs hero-circle">
    <h1 class="hero-title">Velda Nutrition</h1>
    <p class="hero-text">Lorem ipsum dolor sit amet, consectetur adipiscing elit, sed do eiusmod temp</p>
    <a class="pill" style="left:151px;top:301px;width:153px;height:38px;font-size:18px;background:var(--purple)"><span class="pill-dot"></span>Order Now</a>
  </div>
  <div class="abs dots"><span></span><span></span><span></span><span></span><span></span></div>
</section>

<!-- Products -->
<section>
  <h2 class="abs section-title" style="top:862px;font-size:43px">Our Products</h2>

  <div class="arch" style="left:101px;background:var(--purple)"></div>
  <div class="bottle" style="left:158px" role="img" aria-label="MaterniVel pregnancy supplement bottle"></div>
  <h3 class="product-title" style="left:101px">Pregnency Supplements</h3>
  <p class="product-text" style="left:101px">Lorem ipsum dolor sit amet, consectetur<br>adipiscing dolore magna aliqua.</p>
  <a class="btn-order" style="left:180px">ORDER NOW</a>

  <div class="arch" style="left:444px;background:var(--blue)"></div>
  <div class="bottle" style="left:501px" role="img" aria-label="OssaVel bone supplement bottle"></div>
  <h3 class="product-title" style="left:444px">Bone Supplements</h3>
  <p class="product-text" style="left:444px">Lorem ipsum dolor sit amet, consectetur<br>adipiscing dolore magna aliqua.</p>
  <a class="btn-order" style="left:523px">ORDER NOW</a>

  <div class="arch" style="left:789px;background:var(--red)"></div>
  <div class="bottle" style="left:846px" role="img" aria-label="HemaVel iron supplement bottle"></div>
  <h3 class="product-title" style="left:789px">Iron Supplements</h3>
  <p class="product-text" style="left:789px">Lorem ipsum dolor sit amet, consectetur<br>adipiscing dolore magna aliqua.</p>
  <a class="btn-order" style="left:867px">ORDER NOW</a>
</section>

<!-- About -->
<section>
  <svg class="abs" style="left:0;top:1726px" width="1200" height="630" viewBox="0 0 1200 630">
    <defs>
      <linearGradient id="aboutGreen" x1="0" y1="0" x2="1" y2="0">
        <stop offset="0" stop-color="#7fbb33"/>
        <stop offset="1" stop-color="#8cc63f"/>
      </linearGradient>
    </defs>
    <path d="M0 150 C300 50 720 5 1200 8 L1200 560 C900 640 400 640 0 520 Z" fill="#000"/>
    <path d="M0 180 C300 80 720 20 1200 16 L1200 540 C900 640 420 650 0 530 Z" fill="url(#aboutGreen)"/>
    <path d="M0 530 C420 650 900 640 1200 540 L1200 630 L0 630 Z" fill="#fff"/>
    <path d="M0 510 C150 560 250 580 330 590 C200 585 100 570 0 555 Z" fill="#000"/>
  </svg>
  <h2 class="abs about-title">About Us</h2>
  <p class="abs about-text">Lorem ipsum dolor sit amet, consectetur adipiscing elit, sed do eiusmod tempor incididunt ut labore et dolore magna aliqua. Ut enim ad minim veniam, quis nostrud exercitation ullamco laboris nisi ut aliquip ex ea commodo consequat. Duis aute irure dolor in reprehenderit in voluptate velit esse cillum dolore eu fugiat nulla pariatur. Excepteur sint occaecat cupidatat non proident, sunt in culpa qui officia deserunt mollit anim id est laborum.Sed ut ipsa dicta sunt explicabo.</p>
  <a class="abs btn-outline">READ MORE</a>
</section>

<!-- Health -->
<section>
  <div class="abs health-photo" role="img" aria-label="Pregnant woman on a sofa holding a glass of water and a supplement bottle"></div>
  <h2 class="abs health-title">Our products how<br>to help’s your health?</h2>
  <p class="abs health-text">Lorem ipsum dolor sit amet, consectetur adipiscing elit, sed do eiusmod tempor incididunt ut labore et dolore magna aliqua. Ut enim ad minim veniam, quis nostrud exercitation ullamco laboris nisi ut aliquip ex ea commodo consequat. Duis aute irure dolor in reprehenderit in voluptate velit esse cillum.</p>
  <a class="pill" style="left:126px;top:2744px;width:152px;height:39px;font-size:18px"><span class="pill-dot"></span>Read More</a>
</section>

<!-- Gallery -->
<section>
  <h2 class="abs section-title" style="top:3024px;font-size:56px">Our Gallery</h2>
  <div class="gallery-item" style="left:108px;top:3137px;width:308px;height:433px;background:linear-gradient(160deg,#6f7f8c,#c7ccd0 50%,#3f4b57)" role="img" aria-label="Pregnant woman by a window holding tablets"></div>
  <div class="gallery-item" style="left:454px;top:3137px;width:310px;height:198px;background:linear-gradient(180deg,#b9c6d6,#e9c89c 60%,#6d5a4a)" role="img" aria-label="Couple jogging at sunrise"></div>
  <div class="gallery-item" style="left:454px;top:3371px;width:310px;height:199px;background:linear-gradient(160deg,#a58e7c,#e4dfd9 50%,#3fa7a6)" role="img" aria-label="Woman meditating in a teal top"></div>
  <div class="gallery-item" style="left:799px;top:3137px;width:308px;height:433px;background:linear-gradient(180deg,#9fb7c8,#6f7a5c 45%,#c0457a)" role="img" aria-label="Woman stretching outdoors in a pink top"></div>
</section>

<!-- Newsletter -->
<section class="abs newsletter">
  <h2 class="news-title">Sign Up Newsletter</h2>
  <p class="news-text">Lorem ipsum dolor sit amet, consectetur adipiscing elit, sed do eiusmod tempor</p>
  <div class="news-input">Email:</div>
  <a class="news-btn">SIGN UP!</a>
</section>

<!-- Footer -->
<footer>
  <div class="abs brand" style="left:103px;top:4000px;font-size:50px">
    <span class="brand-dot" style="width:64px;height:64px"></span>
    <span class="brand-name">Velda<small>NUTRITION</small></span>
  </div>
  <span class="social" style="left:121px" aria-label="Social profile"></span>
  <span class="social" style="left:171px" aria-label="Social profile"></span>
  <span class="social" style="left:221px" aria-label="Social profile"></span>
  <span class="social" style="left:271px" aria-label="Social profile"></span>

  <h4 class="foot-head" style="left:466px">Navigation</h4>
  <ul class="foot-list" style="left:468px">
    <li>Home</li><li>About</li><li>Supplements</li><li>Features</li><li>Ingrediants</li><li>Contact</li>
  </ul>

  <h4 class="foot-head" style="left:671px">Contact Us</h4>
  <div class="contact-row" style="top:4044px">
    <svg width="24" height="26" viewBox="0 0 24 26"><path d="M12 1a9 9 0 0 0-9 9c0 7 9 15 9 15s9-8 9-15a9 9 0 0 0-9-9z" fill="var(--green)"/><circle cx="12" cy="10" r="3.5" fill="#fff"/></svg>
    <span>123 ipsum dolor sit<br>amet, consectetur<br>adipiscing elit,</span>
  </div>
  <div class="contact-row" style="top:4128px">
    <svg width="24" height="24" viewBox="0 0 24 24"><circle cx="12" cy="12" r="12" fill="var(--green)"/><path d="M8 6l2.5 3-1.5 1.5c.8 1.8 2.2 3.2 4 4l1.5-1.5 3 2.5-1.5 2.5c-4.5 0-9.5-5-9.5-9.5z" fill="#fff"/></svg>
    <span>888 888 8888</span>
  </div>
  <div class="contact-row" style="top:4170px">
    <svg width="24" height="24" viewBox="0 0 24 24"><circle cx="12" cy="12" r="12" fill="var(--green)"/><rect x="6" y="8" width="12" height="8" fill="none" stroke="#fff" stroke-width="1.5"/><path d="M6 8l6 5 6-5" fill="none" stroke="#fff" stroke-width="1.5"/></svg>
    <span>Company@123.com</span>
  </div>

  <h4 class="foot-head" style="left:924px">Our Services</h4>
  <ul class="foot-list" style="left:930px">
    <li>Multivitamins</li><li>Minerals</li><li>Nutritional Supplements</li><li>Pregnency Supplements</li><li>Bone Supplements</li><li>Iron Supplements</li>
  </ul>

  <p class="abs copyright">Copyright © 2022 VELDA NUTRITION. All rights reserved.</p>
</footer>

</body>
</html>
```